Wordpress Design for my Consulting Company

We want a WordPress site created for our new business. We have created a mock-up of the content we want on the site at https://marcusdellow.example-sites.com/website-5

We are not attached to any of the pictures and just put stock stuff from wix's editor, which we don't have rights to use outside of wix.

We are NOT looking to just port this site to WordPress, we are looking for some creative ways to display the content in a more professional artistic sense.

I have included several logo files and a text file with the colors and Fonts used in the logo. We are not looking to change the logo or the colors used in the logo.

The Schedule appointment links to a page that embeds a bookingnest.example.com calendar. https://bookingnest.example.com/marcus-dellow/brightvale

The final website domain will be enterprisebrightvale.example

Enterprise brightvale is a consulting company that works directly with the business owners and leaders of small businesses between 50-200 employees. We help companies make sure they have the right technology to meet their strategic goals. We are the anti-"Computer Guy" and we focus on business outcomes NOT cool technology gadgets.

The final design should communicate business growth and success.

Target Market(s)

Business Owners of companies with 50-200 employees

Coding

Coded - Design and coding required

Number of Pages Required

1 page

Font styles to use
Serif
Other font styles liked:
• Trajan Pro Bold, Open Sans

Requirements
Must have
• Should focus on consulting rather than technology.
• Should show the customer as the hero and we are just their guide.
• Must use the logo provided and the colors and fonts in the text file provided. Any other colors and fonts must be complementary.
• The design should scale for all devices computer, iPad, or phone
Should not have
• Should not focus on technology, we are the anti-"Computer Guy" and we focus on business outcomes NOT cool technology gadgets.

```html
<!DOCTYPE html>
<html lang="en">
<head>
<meta charset="utf-8">
<title>Enterprise Brightvale — Services &amp; Projects</title>
<link rel="stylesheet" href="https://fonts.googleapis.com/css2?family=Poppins:wght@500;600&family=Rubik:wght@400;500&display=swap">
<style>
  :root {
    --sidebar-bg: #ffffff;
    --header-bg: #333333;
    --footer-bg: #37444b;
    --ink: #333333;
    --body-ink: #3f3f3f;
    --accent: #c0713f;
    --card-bg: rgba(255, 255, 255, 0.86);
    --rule-light: #cfcfcf;
    --rule-dark: #333333;
  }
  * { box-sizing: border-box; margin: 0; padding: 0; }
  html, body { width: 1200px; height: 608px; overflow: hidden; background: #ffffff; }
  body { position: relative; font-family: "Rubik", Arial, sans-serif; color: var(--ink); }

  .sidebar {
    position: absolute; left: 0; top: 0; width: 64px; height: 608px;
    background: var(--sidebar-bg);
  }
  .menu-toggle { position: absolute; left: 23px; top: 20px; width: 17px; height: 14px; }
  .sidebar-credit {
    position: absolute; left: 32px; top: 262px;
    transform: translate(-50%, -50%) rotate(-90deg);
    white-space: nowrap; font-size: 8.5px; letter-spacing: 0.4px; color: var(--ink);
  }
  .sidebar-rule { position: absolute; left: 31px; top: 323px; width: 1px; height: 50px; background: var(--rule-light); }
  .sidebar-rule::before { content: ""; position: absolute; left: 0; top: 0; width: 1px; height: 25px; background: var(--rule-dark); }

  .top-band { position: absolute; left: 64px; top: 0; width: 1136px; height: 63px; background: var(--header-bg); }
  .bottom-band { position: absolute; left: 64px; top: 537px; width: 1136px; height: 71px; background: var(--footer-bg); }

  .feature { position: absolute; top: 63px; height: 474px; width: 568px; }
  .feature--services { left: 64px; }
  .feature--projects { left: 632px; }
  .feature-photo { position: absolute; inset: 0; }
  .feature--services .feature-photo {
    background: linear-gradient(160deg, #d7dcd6 0%, #c9cfc6 30%, #d9d3cd 60%, #bfc6c8 100%);
  }
  .feature--projects .feature-photo {
    background: linear-gradient(200deg, #e6ebee 0%, #d2d7d6 35%, #c3c1b9 70%, #a9a9a3 100%);
  }

  .feature-card {
    position: absolute; width: 409px; background: var(--card-bg);
    display: flex; flex-direction: column; align-items: center; justify-content: center;
    text-align: center; padding: 0 6px;
  }
  .feature--services .feature-card { left: 79px; top: 72px; height: 329px; }
  .feature--projects .feature-card { left: 79px; top: 68px; height: 337px; }
  .feature-title { font-family: "Poppins", Arial, sans-serif; font-weight: 600; font-size: 30px; color: var(--ink); margin-bottom: 12px; }
  .feature-text { font-size: 13.6px; line-height: 23.5px; color: var(--body-ink); }
  .feature-text + .feature-text { margin-top: 4px; }
  .feature-button {
    margin-top: 30px; display: inline-flex; align-items: center; justify-content: center; gap: 7px;
    width: 136px; height: 39px; border: 1px solid var(--accent); border-radius: 20px;
    font-family: "Rubik", Arial, sans-serif; font-weight: 500; font-size: 11.8px; color: var(--ink);
    text-decoration: none;
  }

  .back-to-top {
    position: absolute; left: 1133px; top: 541px; width: 42px; height: 42px;
    border: 1px solid var(--accent); border-radius: 50%;
    display: flex; align-items: center; justify-content: center;
  }
</style>
</head>
<body>
  <aside class="sidebar">
    <svg class="menu-toggle" viewBox="0 0 17 14" aria-label="Menu">
      <rect y="1" width="17" height="1.4" fill="#333"/>
      <rect y="6.3" width="17" height="1.4" fill="#333"/>
      <rect y="11.6" width="17" height="1.4" fill="#333"/>
    </svg>
    <p class="sidebar-credit">© 2018, BRIGHTVALE</p>
    <span class="sidebar-rule"></span>
  </aside>

  <header class="top-band"></header>

  <section class="feature feature--services">
    <div class="feature-photo" role="img" aria-label="Photo of a team meeting around a table in a bright office with shelves and plants"></div>
    <div class="feature-card">
      <h2 class="feature-title">Services</h2>
      <p class="feature-text">We offer a complete and tailor made solutions, from planning and creative direction all the way through to post-production and delivery.</p>
      <a class="feature-button" href="#services">
        <svg width="11" height="10" viewBox="0 0 11 10"><path d="M0 5h10M6 1l4 4-4 4" fill="none" stroke="#333" stroke-width="1.2"/></svg>
        View Services
      </a>
    </div>
  </section>

  <section class="feature feature--projects">
    <div class="feature-photo" role="img" aria-label="Photo of colleagues working together in an open office with large windows"></div>
    <div class="feature-card">
      <h2 class="feature-title">Projects</h2>
      <p class="feature-text">Looking for some inspiration?</p>
      <p class="feature-text">Take a look at our previous projects and the innovative solutions that have helped these business.</p>
      <a class="feature-button" href="#projects">
        <svg width="11" height="10" viewBox="0 0 11 10"><path d="M0 5h10M6 1l4 4-4 4" fill="none" stroke="#333" stroke-width="1.2"/></svg>
        View Projects
      </a>
    </div>
  </section>

  <footer class="bottom-band"></footer>

  <a class="back-to-top" href="#top" aria-label="Back to top">
    <svg width="10" height="16" viewBox="0 0 10 16"><path d="M5 16V1M1 5l4-4 4 4" fill="none" stroke="#c0713f" stroke-width="1"/></svg>
  </a>
</body>
</html>
```